Girls Night Out Flyer for a female oriented event

I need a flyer to promote my event which should look "FUN" and "Sophisticated"
I would need the flyer to be 8 1/2" X 11" 300 dpi. I would need the layered .psd file as well as all the fonts. The flyer should contain the following info:

Velvet Evening Soiree CT
Friday, September 25th
6:00-10:00 PM
The Willow Hall Pavilion
14 Marlow Rd
Danbury, CT 06811
First 100 guests will have a chance to win $25,000 and receive a swag bag filled with gifts
$20 Advanced Admission at www.velveteveningsoireect.com
$25 at the door
(Key words)
Martini Bar
Wine Tasting
Food Sampling
Beauty Make-Overs
Fashion Shows
Psychic Readings
Shopping
Door Prizes
Swag Bag
Exhibitors
For tickets visit www.velveteveningsoireect.com

Target Market(s)

Ladies

Industry/Entity Type

Event

Requirements
Must have
• see description

```html
<!DOCTYPE html>
<html lang="en">
<head>
<meta charset="utf-8">
<title>Velvet Evening Soiree CT — Flyer</title>
<link rel="stylesheet" href="https://fonts.googleapis.com/css2?family=Nunito:wght@800;900&family=Questrial&display=swap">
<style>
  :root {
    --night: #050303;
    --party-red: #e0101e;
    --party-red-deep: #a3000c;
    --neon-green: #1f9a12;
    --neon-green-light: #3ccf22;
    --neon-green-dark: #0b5c06;
    --neon-lime: #8dfc4a;
    --sun-yellow: #fbf21a;
    --sun-yellow-deep: #e3d600;
    --price-red: #b0000c;
    --paper: #ffffff;
    --venue-orange: #d98a3a;
  }
  * { margin: 0; padding: 0; box-sizing: border-box; }
  html, body { width: 927px; height: 1200px; overflow: hidden; background: var(--night); }
  .flyer {
    position: relative;
    width: 927px;
    height: 1200px;
    overflow: hidden;
    background: var(--night);
    font-family: "Questrial", "Century Gothic", Arial, sans-serif;
  }
  .hero-photo {
    position: absolute;
    inset: 0;
    background:
      radial-gradient(circle at 220px 210px, rgba(190,170,140,0.55) 0 110px, transparent 190px),
      radial-gradient(ellipse 260px 420px at 390px 620px, rgba(201,138,46,0.75), transparent 75%),
      radial-gradient(ellipse 200px 260px at 360px 300px, rgba(230,170,90,0.55), transparent 80%),
      radial-gradient(circle at 200px 840px, rgba(255,255,255,0.85) 0 18px, rgba(255,255,255,0.15) 70px, transparent 130px),
      radial-gradient(circle at 400px 40px, rgba(255,255,255,0.9) 0 16px, rgba(255,255,255,0.15) 60px, transparent 110px),
      radial-gradient(circle at 860px 345px, rgba(255,210,120,0.9) 0 10px, rgba(255,150,40,0.3) 50px, transparent 110px),
      linear-gradient(180deg, #0b0605 0%, #1a0c06 45%, #0a0504 100%);
  }
  .date-badge {
    position: absolute;
    left: 585px; top: 45px;
    width: 322px; height: 322px;
    border-radius: 50%;
    background: radial-gradient(circle at 50% 40%, #ff2a35, var(--party-red) 55%, var(--party-red-deep));
    box-shadow: 0 0 18px 4px rgba(255,40,50,0.7);
    color: var(--paper);
    text-align: center;
  }
  .date-day { position: absolute; top: 78px; width: 100%; font-size: 66px; letter-spacing: 1px; color: #f6ecec; }
  .date-month { position: absolute; top: 160px; width: 100%; font-size: 33px; font-weight: 700; -webkit-text-stroke: 0.8px var(--paper); }
  .date-time { position: absolute; top: 212px; width: 100%; font-size: 27px; -webkit-text-stroke: 0.5px var(--paper); }
  .event-title {
    position: absolute;
    left: 462px; top: 600px;
    transform: translate(-50%, -50%) rotate(-33deg);
    text-align: center;
    font-family: "Nunito", Arial, sans-serif;
    font-weight: 900;
    font-size: 100px;
    line-height: 0.98;
    text-transform: uppercase;
    white-space: nowrap;
    color: var(--neon-green);
    text-shadow:
      3px 0 0 var(--neon-lime), -3px 0 0 var(--neon-lime),
      0 3px 0 var(--neon-lime), 0 -3px 0 var(--neon-lime),
      2px 2px 0 var(--neon-lime), -2px -2px 0 var(--neon-lime),
      2px -2px 0 var(--neon-lime), -2px 2px 0 var(--neon-lime),
      0 0 14px rgba(141,252,74,0.85),
      0 0 26px rgba(80,220,40,0.5);
  }
  .price-badge {
    position: absolute;
    left: 648px; top: 722px;
    width: 236px; height: 236px;
    border-radius: 50%;
    background: radial-gradient(circle at 50% 45%, #ffff5a, var(--sun-yellow) 55%, var(--sun-yellow-deep));
    box-shadow: 0 0 16px 4px rgba(251,242,26,0.65);
    text-align: center;
    color: var(--price-red);
  }
  .price-amount { font-family: "Nunito", Arial, sans-serif; font-size: 58px; font-weight: 900; line-height: 1; }
  .price-advance { position: absolute; top: 32px; width: 100%; }
  .price-door { position: absolute; top: 138px; width: 100%; }
  .price-note { font-size: 11.5px; line-height: 1.5; margin-top: 2px; -webkit-text-stroke: 0.3px var(--price-red); }
  .price-note .site { font-size: 9.5px; }
  .giveaway-bar {
    position: absolute;
    left: 38px; top: 1020px;
    width: 854px; height: 62px;
    border-radius: 12px;
    background: linear-gradient(180deg, #ffff6a, var(--sun-yellow) 50%, var(--sun-yellow-deep));
    box-shadow: 0 0 14px 4px rgba(251,242,26,0.7);
    color: var(--price-red);
    font-size: 14.5px;
    letter-spacing: 0.2px;
    text-transform: uppercase;
    display: flex; align-items: center; justify-content: center;
  }
  .venue-line {
    position: absolute;
    left: 0; top: 1133px;
    width: 927px;
    text-align: center;
    color: #111;
    font-size: 27px;
    font-style: normal;
    text-transform: uppercase;
    white-space: nowrap;
    text-shadow: 0 0 4px #fff, 0 0 8px #fff, 0 0 12px rgba(255,255,255,0.9);
  }
  .venue-name { color: var(--venue-orange); }
</style>
</head>
<body>
<main class="flyer">
  <div class="hero-photo" role="img" aria-label="Photo of a woman in a sequined gold dress dancing under a disco ball with bright club lights"></div>

  <section class="date-badge">
    <div class="date-day">FRIDAY</div>
    <div class="date-month">SEPTEMBER 25TH</div>
    <div class="date-time">6:00-10:00 PM</div>
  </section>

  <h1 class="event-title">Velvet Evening<br>Soiree CT</h1>

  <section class="price-badge">
    <div class="price-advance">
      <div class="price-amount">$20</div>
      <div class="price-note">Advanced Admission<br><span class="site">at www.velveteveningsoireect.com</span></div>
    </div>
    <div class="price-door">
      <div class="price-amount">$25</div>
      <div class="price-note">at the door</div>
    </div>
  </section>

  <div class="giveaway-bar">First 100 guests will have a chance to win $25,000 and receive a swag bag filled with gifts</div>

  <address class="venue-line">The <span class="venue-name">Willow Hall Pavilion</span> 14 Marlow Rd Danbury, CT 06811</address>
</main>
</body>
</html>
```